依頼詳細
バイクで周辺のニュータウンに配布を考えています。
量販店よりもかなり安いので、安いとわかるようなチラシに仕上げたいです。
また、片面にウォーターサーバーのサブスクの内容を入れてます。
デザインは近いものでイラストを考えています。
記載項目
社名・電話番号・料金プラン
エアコンの取付・取外しをお得にできます。
エアコン基本設置4m 11,000円~
エアコン基本外し 4,000円(2台台以上)
(外し単品は6,000円)
価格は税込み
サイズ
A5
ページ数
片面
希望イメージ
シンプル 複雑
単色 カラフル
暗い 明るい
日常 高級
遊び心 厳粛
未来的 伝統的
女性的 男性的
希望する色
黄・オレンジ系
納品ファイル
• イラストレーター形式 (.ai)
補足説明
■ 選んだ理由

こちらで想定していたのと全然違う構成に感銘を受けました。
かなり手直しが必要ですが、こちらの路線でチラシを作成しようと思います。

■ 提案者全員のお礼・コメント

今回はたくさんのご応募をいただき大変感謝しております。
たくさんのパターンがあり感動しています。
また、同じような応募をしますのでその際はよろしくお願いいたします

```html
<!DOCTYPE html>
<html lang="ja">
<head>
<meta charset="utf-8">
<title>エアコンの取付・取外し 料金案内チラシ</title>
<link href="https://fonts.googleapis.com/css2?family=M+PLUS+Rounded+1c:wght@500;700;800;900&display=swap" rel="stylesheet">
<style>
  :root {
    --cream: #fff7e6;
    --sunny: #fde3b0;
    --sunny-deep: #f9d28e;
    --orange: #f08a1c;
    --orange-dark: #e06f0c;
    --red: #e0312b;
    --ink: #4a3526;
    --white: #ffffff;
  }
  * { box-sizing: border-box; margin: 0; padding: 0; }
  html, body { width: 847px; height: 1200px; overflow: hidden; background: var(--white); }
  body { font-family: "M PLUS Rounded 1c", sans-serif; color: var(--ink); }

  .flyer {
    position: relative;
    width: 847px;
    height: 1200px;
    background: linear-gradient(180deg, var(--cream) 0%, var(--cream) 18%, var(--sunny) 40%, var(--sunny) 82%, var(--white) 82%);
    overflow: hidden;
  }

  /* Feature badges */
  .features {
    position: absolute;
    top: 14px; left: 28px; right: 28px;
    display: flex; justify-content: space-between;
    list-style: none;
  }
  .feature {
    width: 236px; height: 56px;
    background: var(--red);
    color: var(--white);
    display: flex; align-items: center; justify-content: center; gap: 14px;
    font-size: 32px; font-weight: 800; letter-spacing: 4px;
    clip-path: polygon(0 0, 100% 0, 96% 50%, 100% 100%, 0 100%, 4% 50%);
  }
  .feature svg { width: 32px; height: 26px; }

  /* Headline */
  .headline {
    position: absolute;
    top: 112px; left: 0; right: 0;
    text-align: center;
    font-weight: 900;
    line-height: 1.25;
    white-space: nowrap;
  }
  .headline .line { display: block; font-size: 72px; color: var(--orange-dark); letter-spacing: 1px; }
  .headline .small { font-size: 54px; color: var(--ink); }
  .headline .line-2 { color: var(--ink); }
  .headline .accent { color: var(--orange-dark); }

  /* Illustration placeholder */
  .scene {
    position: absolute;
    top: 300px; left: 60px;
    width: 727px; height: 430px;
    background: radial-gradient(ellipse at 50% 40%, #fff3da 0%, var(--sunny-deep) 80%);
    border-radius: 24px;
  }

  /* Price panel */
  .pricing {
    position: absolute;
    top: 760px; left: 100px;
    width: 648px; height: 210px;
    background: var(--white);
    border-radius: 6px;
  }
  .pricing-tab {
    position: absolute;
    top: -26px; left: 0;
    background: var(--orange);
    color: var(--white);
    padding: 6px 22px 6px 26px;
    border-radius: 6px 6px 6px 0;
    font-size: 30px; font-weight: 800; letter-spacing: 2px;
    display: flex; align-items: baseline; gap: 12px;
    white-space: nowrap;
  }
  .pricing-tab small { font-size: 13px; font-weight: 700; letter-spacing: 0; }
  .price-list { list-style: none; padding: 54px 20px 0 28px; }
  .price-row {
    display: flex; align-items: center;
    font-weight: 800;
    margin-bottom: 30px;
    white-space: nowrap;
  }
  .price-row > * { flex-shrink: 0; }
  .price-row .mark { width: 20px; height: 20px; background: var(--ink); margin-right: 14px; }
  .price-row .name { font-size: 28px; width: 272px; }
  .price-row .name .unit { font-size: 22px; }
  .price-row .amount { font-size: 40px; color: var(--orange-dark); letter-spacing: 1px; line-height: 1; }
  .price-row .amount .yen { font-size: 30px; }
  .price-row .note { font-size: 12px; font-weight: 700; line-height: 1.45; margin-left: 16px; color: var(--ink); }

  /* Call to action */
  .cta {
    position: absolute;
    top: 990px; left: 100px;
    width: 648px; height: 52px;
    background: var(--orange);
    border-radius: 26px;
    color: var(--white);
    font-size: 30px; font-weight: 800;
    display: flex; align-items: center; justify-content: center;
    letter-spacing: 2px;
    white-space: nowrap;
  }

  /* Footer */
  .footer {
    position: absolute;
    top: 1090px; left: 28px; right: 28px;
    height: 80px;
    display: flex; align-items: center; justify-content: space-between;
    white-space: nowrap;
  }
  .company { font-weight: 900; display: flex; align-items: baseline; gap: 8px; }
  .company .kind { font-size: 24px; }
  .company .name { font-size: 46px; }
  .phone { display: flex; align-items: center; gap: 10px; color: var(--orange-dark); font-weight: 900; font-size: 52px; }
  .phone svg { width: 48px; height: 48px; }
</style>
</head>
<body>
<main class="flyer">
  <ul class="features">
    <li class="feature"><svg viewBox="0 0 32 26"><path d="M2 6l7 7 7-11 7 11 7-7-3 18H5z" fill="#fff"/></svg>格安</li>
    <li class="feature"><svg viewBox="0 0 32 26"><path d="M2 6l7 7 7-11 7 11 7-7-3 18H5z" fill="#fff"/></svg>迅速</li>
    <li class="feature"><svg viewBox="0 0 32 26"><path d="M2 6l7 7 7-11 7 11 7-7-3 18H5z" fill="#fff"/></svg>丁寧</li>
  </ul>

  <h1 class="headline">
    <span class="line">エアコン<span class="small">の</span>取付・取外し</span>
    <span class="line line-2"><span class="accent">お得</span>にできます！</span>
  </h1>

  <div class="scene" role="img" aria-label="壁のエアコンを取り付ける作業員と、それを見守る女性のイラスト"></div>

  <section class="pricing">
    <h2 class="pricing-tab">料金プラン<small>※価格は税込み</small></h2>
    <ul class="price-list">
      <li class="price-row">
        <span class="mark"></span>
        <span class="name">エアコン基本設置 <span class="unit">4m</span></span>
        <span class="amount">11,000<span class="yen">円〜</span></span>
      </li>
      <li class="price-row">
        <span class="mark"></span>
        <span class="name">エアコン基本外し</span>
        <span class="amount">4,000<span class="yen">円</span></span>
        <span class="note">※2台以上<br>※外し単品は6,000円</span>
      </li>
    </ul>
  </section>

  <p class="cta">まずは、お気軽にご相談ください！</p>

  <footer class="footer">
    <p class="company"><span class="kind">株式会社</span><span class="name">エアコン取付</span></p>
    <p class="phone">
      <svg viewBox="0 0 48 48"><path d="M14 6c2 0 3 1 4 3l3 7c1 2 0 3-1 4l-3 3c2 5 6 9 11 11l3-3c1-1 2-2 4-1l7 3c2 1 3 2 3 4v5c0 2-2 4-4 4C20 46 2 28 2 8c0-2 2-4 4-4z" fill="currentColor"/></svg>
      000-000-000
    </p>
  </footer>
</main>
</body>
</html>
```